Dental office mass mail marketing

Picture of smiling group. I want to write on the card an offer which is $100 credit with new patient appointment. No cash and some restrictions may apply.
I have couple designs u may be able yo use.

Reason: Chance to see more designs.

Industry/Entity Type

Marketing

Font styles to use
Sans Serif

Colors
33a6d7
3377b5

```html
<!DOCTYPE html>
<html lang="en">
<head>
<meta charset="utf-8">
<title>Brightline Dentistry – New Patient Postcard</title>
<link rel="stylesheet" href="https://fonts.googleapis.com/css2?family=Questrial&display=swap">
<style>
  :root {
    --backdrop: #1d1b1a;
    --blue-header: #2379c2;
    --blue-text: #1e7cc4;
    --navy-text: #1d4f8a;
    --paper: #ffffff;
    --panel-grey: #e4e4e4;
    --rule: #555555;
    --ink: #222222;
  }
  * { box-sizing: border-box; margin: 0; padding: 0; }
  html, body {
    width: 764px; height: 1200px; overflow: hidden;
    background: var(--backdrop);
    font-family: "Questrial", "Century Gothic", sans-serif;
    font-weight: 400;
  }
  .postcard {
    position: absolute; left: 20px; width: 718px; overflow: hidden;
    background: var(--paper);
  }
  .postcard--front { top: 20px; height: 555px; }
  .postcard--back { top: 612px; height: 558px; }
  .postcard__art { position: absolute; inset: 0; }

  .tagline {
    position: absolute; left: 24px; top: 31px;
    color: var(--paper); font-size: 15px; letter-spacing: 0.2px;
  }
  .brand {
    position: absolute; color: var(--paper); text-align: center; line-height: 1; font-weight: 400;
  }
  .brand--front { right: 40px; top: 40px; font-size: 44px; width: 260px; }
  .brand--back { left: 26px; top: 36px; font-size: 30px; width: 170px; }
  .brand small {
    display: block; font-size: 0.42em; letter-spacing: 3px; margin-top: 8px;
  }

  .headline {
    position: absolute; right: 21px; top: 278px; text-align: right;
    color: var(--blue-text); font-size: 36px; line-height: 1.18; font-weight: 400;
  }
  .subhead {
    position: absolute; right: 26px; top: 392px; text-align: right;
    color: var(--blue-text); font-size: 23px; line-height: 1.3;
  }

  .offer {
    position: absolute; left: 0; top: 214px; width: 340px;
    text-align: center; color: var(--blue-text);
  }
  .offer__amount { font-size: 42px; line-height: 1.05; }
  .offer__detail { font-size: 25px; line-height: 1.3; }
  .offer__terms { font-size: 17px; line-height: 1.4; margin-top: 10px; }
  .offer__phone { font-size: 42px; margin-top: 12px; line-height: 1.1; }
  .offer__address { font-size: 15px; color: var(--navy-text); margin-top: 2px; }

  .mail-panel {
    position: absolute; background: var(--panel-grey);
    font-family: Arial, sans-serif; font-size: 9px; color: var(--ink); text-align: center;
  }
  .mail-panel--postage { left: 540px; top: 0; width: 178px; height: 176px; padding-top: 85px; }
  .mail-panel--address { left: 347px; top: 179px; width: 371px; height: 280px; padding-top: 33px; }
  .mail-panel--barcode { left: 87px; top: 469px; width: 631px; height: 89px; padding-top: 38px; }
  .address-lines { list-style: none; margin: 20px auto 0; width: 314px; }
  .address-lines li { border-top: 2px solid var(--rule); height: 33px; }
</style>
</head>
<body>

<section class="postcard postcard--front">
  <svg class="postcard__art" width="718" height="555" viewBox="0 0 718 555">
    <defs>
      <linearGradient id="sky" x1="0" y1="0" x2="1" y2="1">
        <stop offset="0" stop-color="#d9a98c"/>
        <stop offset="0.4" stop-color="#c9a3c4"/>
        <stop offset="0.7" stop-color="#bcd3ea"/>
        <stop offset="1" stop-color="#a9c8ea"/>
      </linearGradient>
    </defs>
    <g role="img" aria-label="Photo of four smiling friends huddled together against a bright cloudy sky">
      <rect x="0" y="120" width="718" height="435" fill="url(#sky)"/>
    </g>
    <path class="header-band" d="M0 0 H718 V230 C480 250 240 170 0 190 Z" fill="var(--blue-header)"/>
  </svg>

  <p class="tagline">Healthy Mind • Healthy Body • Healthy Smile</p>
  <p class="brand brand--front">Brightline<small>DENTISTRY</small></p>

  <h1 class="headline">A Healthy Smile<br>Starts Here!</h1>
  <p class="subhead">See Our<br>Special Offer for<br>New Patients!</p>
</section>

<section class="postcard postcard--back">
  <svg class="postcard__art" width="718" height="558" viewBox="0 0 718 558">
    <path class="header-band" d="M0 0 H540 V160 C380 120 200 200 0 180 Z" fill="var(--blue-header)"/>
  </svg>

  <p class="brand brand--back">Brightline<small>DENTISTRY</small></p>

  <div class="offer">
    <p class="offer__amount">$100 Credit</p>
    <p class="offer__detail">with new<br>patient appointment</p>
    <p class="offer__terms">Call for details.<br>Some restrictions may apply.</p>
    <p class="offer__phone">000-000-000</p>
    <p class="offer__address">123 Any Street • Any Town, XX 123456</p>
  </div>

  <div class="mail-panel mail-panel--postage">Postage Area</div>
  <div class="mail-panel mail-panel--address">
    Address Area
    <ul class="address-lines"><li></li><li></li><li></li><li></li></ul>
  </div>
  <div class="mail-panel mail-panel--barcode">USPO Barcode Area</div>
</section>

</body>
</html>
```